Valtiro Caribbean Rum Punch Label

Product name:Meridel Cove Rum Punch

Type of product: Bottled Rum punch in flavors such as mango, passion fruit, melon and pina colada. It is delightful blend of Bellamore light rums which come in a variety of trpoical and natural flavors.

The bottle has an existing label design which is quite dated. Client wishes a new logo design. Must position the brand as premium and keep its Caribbean identity. Designers have the creative freedom to explore as many creative options as possible.

The challenge: for it to maintain its Caribbean identity but not look cliched with the generic Caribbean-type imagery as this has been done before. Though it is Caribbean born...it should also have an international look and feel to it.

Attachment: See the attachment. Client thought this was a bit "simple" and wanted more of a "premium" look for the brand.

```html
<!DOCTYPE html>
<html lang="en">
<head>
<meta charset="utf-8">
<title>Meridel Cove Rum Punch – Label Range</title>
<link rel="stylesheet" href="https://fonts.googleapis.com/css2?family=Cinzel:wght@400;700;900&family=Cormorant+Garamond:wght@500;700&display=swap">
<style>
  :root {
    --bg-melon: #f9ef93;
    --bg-mango: #eea540;
    --bg-pina: #f3d868;
    --melon-light: #f7e43a;
    --melon-dark: #d9b607;
    --melon-ink: #3f9a2a;
    --mango-light: #ee5a32;
    --mango-dark: #c22714;
    --mango-ink: #c0271a;
    --pina-light: #b4641c;
    --pina-dark: #6a2c0c;
    --pina-ink: #a86a12;
    --white: #ffffff;
    --panel-top: #fbfbfb;
    --panel-bottom: #e4e4e4;
    --rule: #7a7a7a;
    --small-ink: #3a3a3a;
  }
  * { margin: 0; padding: 0; box-sizing: border-box; }
  html, body { width: 1200px; height: 457px; overflow: hidden; }
  body { display: flex; font-family: "Cormorant Garamond", Georgia, serif; }

  .flavour { position: relative; width: 400px; height: 457px; }
  .flavour--melon { background: var(--bg-melon); --light: var(--melon-light); --dark: var(--melon-dark); --ink: var(--melon-ink); --band-ink: var(--melon-ink); }
  .flavour--mango { background: var(--bg-mango); --light: var(--mango-light); --dark: var(--mango-dark); --ink: var(--mango-ink); --band-ink: var(--white); }
  .flavour--pina  { background: var(--bg-pina);  --light: var(--pina-light);  --dark: var(--pina-dark);  --ink: var(--pina-ink);  --band-ink: var(--white); }

  .butterfly {
    position: absolute; left: 174px; top: 10px; width: 54px; height: 62px; z-index: 3;
    background: radial-gradient(ellipse at 50% 50%, #f4a23a 0%, #e06a1c 60%, #b2470f 100%);
    border-radius: 50% 50% 45% 45%;
  }

  .crest { position: absolute; left: 73px; top: 56px; width: 257px; height: 156px; }
  .crest svg { position: absolute; inset: 0; }
  .crest__name {
    position: absolute; left: 0; right: 0; top: 16px; text-align: center;
    font-family: "Cinzel", Georgia, serif; font-weight: 400; color: var(--white);
    line-height: 0.92;
  }
  .crest__line1 { display: block; font-size: 40px; letter-spacing: -0.5px; }
  .crest__line2 { display: block; font-size: 56px; }
  .crest__sub {
    position: absolute; left: 48px; right: 30px; top: 120px;
    display: flex; align-items: center; gap: 6px;
    font-family: "Cinzel", Georgia, serif; font-size: 11px; line-height: 1; color: var(--white); letter-spacing: 0.8px;
  }
  .crest__sub::before { content: ""; width: 62px; height: 1px; background: var(--white); }

  .panel {
    position: absolute; left: 90px; top: 206px; width: 217px; height: 175px;
    background: var(--white); padding: 4px;
  }
  .panel__inner {
    position: relative; width: 100%; height: 100%;
    background: linear-gradient(180deg, var(--panel-top), var(--panel-bottom));
  }
  .panel__flavour {
    position: absolute; left: 0; right: 0; top: 8px; text-align: center;
    font-family: "Cinzel", Georgia, serif; font-weight: 900; font-size: 31px;
    color: var(--ink); letter-spacing: 1px;
  }
  .flavour--mango .panel__flavour { font-weight: 400; letter-spacing: 5px; }
  .flavour--pina .panel__flavour { font-size: 24px; top: 14px; letter-spacing: 0; }
  .panel__fruit {
    position: absolute; left: 48px; top: 50px; width: 112px; height: 78px; border-radius: 50%;
  }
  .flavour--melon .panel__fruit { background: radial-gradient(ellipse at 45% 40%, #fff36a, #f0cf10 70%, #6aa23a); }
  .flavour--mango .panel__fruit { background: radial-gradient(ellipse at 40% 55%, #f6c24a, #e4601c 70%, #5e8a3a); }
  .flavour--pina  .panel__fruit { background: radial-gradient(ellipse at 65% 50%, #f3c53a, #8b5226 70%, #4e8a32); }
  .panel__serve {
    position: absolute; left: 14px; right: 14px; top: 132px;
    border-top: 1px solid var(--rule); border-bottom: 1px solid var(--rule);
    display: flex; justify-content: space-between; padding: 3px 0 2px;
    font-family: "Cormorant Garamond", Georgia, serif; font-weight: 500; font-size: 10px; line-height: 1.1; color: var(--small-ink); letter-spacing: 0.5px;
  }
  .panel__spec {
    position: absolute; left: 0; right: 0; top: 153px; text-align: center;
    font-size: 8.5px; line-height: 1; color: var(--small-ink); word-spacing: 4px;
  }
  .panel__spec b { font-weight: 700; }

  .band {
    position: absolute; left: 70px; top: 384px; width: 262px; height: 57px;
    border: 2px solid var(--white); border-radius: 10px;
    background: linear-gradient(180deg, var(--light), var(--dark));
    display: flex; flex-direction: column; justify-content: center; align-items: center; gap: 4px;
    font-family: "Cinzel", Georgia, serif; font-weight: 700; font-size: 10px; line-height: 1; color: var(--band-ink); letter-spacing: 2.4px;
  }
</style>
</head>
<body>

<section class="flavour flavour--melon">
  <div class="butterfly" role="img" aria-label="Butterfly illustration perched on the crest"></div>
  <div class="crest">
    <svg viewBox="0 0 257 156" preserveAspectRatio="none" aria-hidden="true">
      <defs><linearGradient id="crest-melon" x1="0" y1="0" x2="0" y2="1"><stop offset="0" stop-color="#f7e43a"/><stop offset="1" stop-color="#d9b607"/></linearGradient></defs>
      <path d="M12 22 Q128.5 -4 245 22 Q257 24 257 36 L257 140 Q257 152 245 152 Q128.5 138 12 152 Q0 152 0 140 L0 36 Q0 24 12 22 Z" fill="url(#crest-melon)" stroke="#fff" stroke-width="2"/>
    </svg>
    <div class="crest__name"><span class="crest__line1">MERIDEL</span><span class="crest__line2">COVE</span></div>
    <div class="crest__sub"><span>RUM PUNCH</span></div>
  </div>
  <div class="panel"><div class="panel__inner">
    <h2 class="panel__flavour">MELON</h2>
    <div class="panel__fruit" role="img" aria-label="Photograph of a yellow melon with green leaves"></div>
    <p class="panel__serve"><span>SERVE</span><span>OVER</span><span>CRUSHED</span><span>ICE</span></p>
    <p class="panel__spec">17% alc/vol <b>750ml e</b></p>
  </div></div>
  <div class="band"><span>A BLEND OF CARIBBEAN RUM</span><span>&amp; EXOTIC FRUIT FLAVOURS</span></div>
</section>

<section class="flavour flavour--mango">
  <div class="butterfly" role="img" aria-label="Butterfly illustration perched on the crest"></div>
  <div class="crest">
    <svg viewBox="0 0 257 156" preserveAspectRatio="none" aria-hidden="true">
      <defs><linearGradient id="crest-mango" x1="0" y1="0" x2="0" y2="1"><stop offset="0" stop-color="#ee5a32"/><stop offset="1" stop-color="#c22714"/></linearGradient></defs>
      <path d="M12 22 Q128.5 -4 245 22 Q257 24 257 36 L257 140 Q257 152 245 152 Q128.5 138 12 152 Q0 152 0 140 L0 36 Q0 24 12 22 Z" fill="url(#crest-mango)" stroke="#fff" stroke-width="2"/>
    </svg>
    <div class="crest__name"><span class="crest__line1">MERIDEL</span><span class="crest__line2">COVE</span></div>
    <div class="crest__sub"><span>RUM PUNCH</span></div>
  </div>
  <div class="panel"><div class="panel__inner">
    <h2 class="panel__flavour">MANGO</h2>
    <div class="panel__fruit" role="img" aria-label="Photograph of a ripe mango with leaves"></div>
    <p class="panel__serve"><span>SERVE</span><span>OVER</span><span>CRUSHED</span><span>ICE</span></p>
    <p class="panel__spec">17% alc/vol <b>750ml e</b></p>
  </div></div>
  <div class="band"><span>A BLEND OF CARIBBEAN RUM</span><span>&amp; EXOTIC FRUIT FLAVOURS</span></div>
</section>

<section class="flavour flavour--pina">
  <div class="butterfly" role="img" aria-label="Butterfly illustration perched on the crest"></div>
  <div class="crest">
    <svg viewBox="0 0 257 156" preserveAspectRatio="none" aria-hidden="true">
      <defs><linearGradient id="crest-pina" x1="0" y1="0" x2="0" y2="1"><stop offset="0" stop-color="#b4641c"/><stop offset="1" stop-color="#6a2c0c"/></linearGradient></defs>
      <path d="M12 22 Q128.5 -4 245 22 Q257 24 257 36 L257 140 Q257 152 245 152 Q128.5 138 12 152 Q0 152 0 140 L0 36 Q0 24 12 22 Z" fill="url(#crest-pina)" stroke="#fff" stroke-width="2"/>
    </svg>
    <div class="crest__name"><span class="crest__line1">MERIDEL</span><span class="crest__line2">COVE</span></div>
    <div class="crest__sub"><span>RUM PUNCH</span></div>
  </div>
  <div class="panel"><div class="panel__inner">
    <h2 class="panel__flavour">PIÑA COLADA</h2>
    <div class="panel__fruit" role="img" aria-label="Photograph of two coconuts beside a pineapple"></div>
    <p class="panel__serve"><span>SERVE</span><span>OVER</span><span>CRUSHED</span><span>ICE</span></p>
    <p class="panel__spec">17% alc/vol <b>750ml e</b></p>
  </div></div>
  <div class="band"><span>A BLEND OF CARIBBEAN RUM</span><span>&amp; EXOTIC FRUIT FLAVOURS</span></div>
</section>

</body>
</html>
```